Creative modern Trade show booth design for saas software company

We are looking for a simple clean Trade show booth design for our booth. The dimension of the booth are attached for reference. samples of other designs we like are also attached. Our website is in www.trelvix.com. The both consists of two-piece main booth back, a stand and an iPad stand. The booth design showing the Monkey on it is the booth. We would like our logo shown, possibly an image and short description of our services. and maybe images of our reports. please visit our website to get ideas. our main product is Trelvix Software.

Target Market(s)

Insurance agents/ brokers & producers.

Font styles to use
Other font styles liked:
• abadi MT Pro

Colors

Designer to choose colors to be used in the design.

Requirements
Must have
• Our Logo. A creative statement to draw attention. Our 4 sectors of products. Trelvix Software, Trelvix Claims, Trelvix Markets, Trelvix Products

```html
<!DOCTYPE html>
<html lang="en">
<head>
<meta charset="utf-8">
<title>Trelvix Trade Show Booth Graphics</title>
<link rel="stylesheet" href="https://fonts.googleapis.com/css2?family=Jost:ital,wght@0,300;0,500;0,600;0,700;1,500&display=swap">
<style>
  :root {
    --page: #ffffff;
    --sign: #505050;
    --sign-edge: #8fb7d8;
    --blue-deep: #1e5fa8;
    --blue-mid: #4a90d4;
    --blue-light: #bfe0f6;
    --teal: #3f9fc8;
    --ink: #2d2d2d;
    --concrete-a: #9a9a94;
    --concrete-b: #6d6e6a;
    --sheet: #ffffff;
    --monitor: #3a3a3a;
    --monitor-edge: #1f1f1f;
    --chart-blue: #4aa6dd;
    --chart-red: #e5473b;
    --chart-green: #3daa4a;
    --chart-yellow: #f2c230;
    --chart-purple: #6b3f98;
  }
  * { margin: 0; padding: 0; box-sizing: border-box; }
  html, body { width: 1200px; height: 907px; overflow: hidden; background: var(--page); }
  body { position: relative; font-family: "Jost", sans-serif; color: var(--ink); }

  .header-sign {
    position: absolute; left: 560px; top: 84px; width: 358px; height: 72px;
    background: var(--sign); border-radius: 16px; border: 2px solid var(--sign-edge);
    display: flex; align-items: center; justify-content: center;
  }
  .brand { font-family: "Jost", sans-serif; font-weight: 600; letter-spacing: 1px; line-height: 1; }
  .header-sign .brand { color: #fff; font-size: 50px; }

  .tower {
    position: absolute; left: 264px; top: 64px; width: 234px; height: 644px; overflow: hidden;
    background: linear-gradient(180deg, var(--blue-mid) 0%, var(--blue-deep) 40%, var(--blue-light) 62%, #dff0fb 100%);
    border-radius: 6px 6px 0 0;
  }
  .tower svg { position: absolute; inset: 0; }
  .tower .brand { position: absolute; left: 0; right: 0; top: 110px; text-align: center; color: #fff; font-size: 42px; }
  .tower-statement {
    position: absolute; left: 30px; width: 174px; top: 418px; text-align: center;
    font-style: italic; font-weight: 500; font-size: 14px; line-height: 17px; color: var(--ink);
  }
  .tower-steps { position: absolute; left: 58px; top: 476px; list-style: none; font-weight: 300; font-size: 20px; line-height: 24px; color: var(--ink); }
  .tower-steps li::before { content: "•"; display: inline-block; width: 16px; font-size: 18px; }

  .wall-monitor {
    position: absolute; left: 411px; top: 278px; width: 179px; height: 104px;
    background: var(--monitor); border: 2px solid var(--monitor-edge); z-index: 3;
  }

  .back-wall {
    position: absolute; left: 502px; top: 163px; width: 476px; height: 542px; overflow: hidden;
    border-radius: 20px 20px 0 0;
  }
  .back-wall .scene {
    position: absolute; inset: 0;
    background: radial-gradient(ellipse at 35% 35%, var(--concrete-a), var(--concrete-b) 85%);
  }
  .back-wall .scene::after {
    content: ""; position: absolute; left: 0; right: 0; bottom: 0; height: 90px;
    background: linear-gradient(180deg, #6b6b68, #555552);
  }
  .back-wall .figure-area {
    position: absolute; right: 18px; top: 100px; width: 80px; height: 442px;
    background: linear-gradient(180deg, #c9ccd2 0%, #d9dce0 55%, #2b2b30 60%, #2b2b30 100%);
    border-radius: 40px 40px 0 0; opacity: .85;
  }
  .back-wall .brand { position: absolute; left: 128px; top: 120px; font-size: 60px; color: var(--teal); }
  .sectors { position: absolute; left: 122px; top: 192px; display: flex; gap: 0; }
  .sector { width: 84px; text-align: center; }
  .sector svg { display: block; margin: 0 auto; }
  .sector-name { font-weight: 300; font-size: 18px; color: #3a3a3a; line-height: 20px; margin-top: 4px; }
  .sector-detail { font-weight: 700; font-size: 10px; line-height: 12px; color: #1f1f1f; margin-top: 8px; }

  .reports { position: absolute; left: 38px; top: 347px; display: flex; gap: 10px; }
  .report { width: 128px; height: 168px; background: var(--sheet); box-shadow: 0 1px 3px rgba(0,0,0,.35); position: relative; }
  .report-head { display: flex; justify-content: space-between; padding: 5px 5px 0; font-size: 3.5px; color: #3b7fc0; }
  .report-title { padding: 4px 5px 0; font-size: 4px; color: #444; text-transform: uppercase; }
  .report-foot { position: absolute; left: 5px; right: 5px; bottom: 4px; font-size: 3.5px; color: #888; }
  .report svg { display: block; margin: 2px auto 0; }

  .counter {
    position: absolute; left: 142px; top: 565px; width: 312px; height: 315px; overflow: hidden;
    border-radius: 4px; z-index: 4;
  }
  .counter-top { position: absolute; left: 0; right: 0; top: 0; height: 22px; background: #2a2a2a; }
  .counter .scene {
    position: absolute; left: 0; right: 0; top: 22px; bottom: 0;
    background: radial-gradient(ellipse at 40% 40%, var(--concrete-a), var(--concrete-b) 90%);
  }
  .counter .figure-area {
    position: absolute; left: 212px; top: 60px; width: 52px; height: 255px;
    background: linear-gradient(180deg, #c9ccd2 0%, #d9dce0 50%, #2b2b30 56%);
    border-radius: 26px 26px 0 0; opacity: .85;
  }
  .counter .brand { position: absolute; left: 40px; top: 100px; font-size: 36px; color: var(--teal); }
</style>
</head>
<body>

  <div class="header-sign"><span class="brand">trelvix</span></div>

  <section class="tower">
    <svg width="234" height="644" viewBox="0 0 234 644" aria-hidden="true">
      <path d="M0 0 H234 V80 C160 70 70 55 0 90 Z" fill="#7ab3e4"/>
      <path d="M0 240 C60 280 150 270 234 230 V330 C150 290 70 300 0 320 Z" fill="#3a7cc4" opacity=".7"/>
      <path d="M0 320 C80 300 170 300 234 340 V644 H0 Z" fill="#d2ebfa" opacity=".6"/>
    </svg>
    <span class="brand">trelvix</span>
    <p class="tower-statement">Trelvix provides 4 simple steps to grow and retain your book of business!</p>
    <ul class="tower-steps"><li>Analyze</li></ul>
  </section>

  <section class="back-wall">
    <div class="scene" role="img" aria-label="Concrete wall photo with a businesswoman casting a superhero shadow"></div>
    <div class="figure-area" role="img" aria-label="Businesswoman looking into the distance"></div>
    <span class="brand">trelvix</span>

    <div class="sectors">
      <div class="sector">
        <svg width="28" height="28" viewBox="0 0 28 28" fill="none" stroke="#222" stroke-width="1.4" aria-hidden="true">
          <circle cx="14" cy="14" r="12"/><ellipse cx="14" cy="14" rx="5" ry="12"/><path d="M2 14h24M4 8h20M4 20h20"/>
        </svg>
        <div class="sector-name">software</div>
        <div class="sector-detail">Mod Calculator-<br>Analysis &amp;<br>Reports</div>
      </div>
      <div class="sector">
        <svg width="28" height="28" viewBox="0 0 28 28" fill="none" stroke="#222" stroke-width="1.4" aria-hidden="true">
          <path d="M14 2 L24 6 V13 C24 20 19 24 14 26 C9 24 4 20 4 13 V6 Z"/><path d="M14 2 V26"/>
        </svg>
        <div class="sector-name">claims</div>
        <div class="sector-detail">Markets<br>Free Access<br>To Trelvix</div>
      </div>
      <div class="sector">
        <svg width="28" height="28" viewBox="0 0 28 28" fill="none" stroke="#222" stroke-width="1.4" aria-hidden="true">
          <path d="M2 14 C2 6 26 6 26 14 C22 12 18 12 14 14 C10 12 6 12 2 14 Z"/><path d="M14 7 V23 C14 26 10 26 10 23"/>
        </svg>
        <div class="sector-name">markets</div>
        <div class="sector-detail">Individual<br>Claims<br>Management</div>
      </div>
    </div>

    <div class="reports">
      <article class="report">
        <div class="report-head"><span>Agency loss report</span><span>Policy year review</span></div>
        <div class="report-title">Historical Review</div>
        <svg width="110" height="120" viewBox="0 0 110 120" aria-hidden="true">
          <g stroke="#e3e3e3" stroke-width=".5"><path d="M8 10H104M8 25H104M8 40H104M8 55H104"/></g>
          <polyline points="10,48 26,42 42,40 58,36 74,38 90,34 104,33" fill="none" stroke="var(--chart-blue)" stroke-width="1.4"/>
          <polyline points="10,52 26,50 42,49 58,12 74,44 90,46 104,45" fill="none" stroke="var(--chart-red)" stroke-width="1.4"/>
          <polyline points="10,55 26,55 42,55 58,55 74,55 90,55 104,55" fill="none" stroke="var(--chart-green)" stroke-width="1.4"/>
          <g stroke="#e3e3e3" stroke-width=".5"><path d="M8 80H104M8 95H104M8 110H104"/></g>
          <polyline points="10,108 26,104 42,100 58,102 74,80 90,104 104,106" fill="none" stroke="var(--chart-red)" stroke-width="1.4"/>
          <polyline points="10,110 26,110 42,109 58,108 74,104 90,108 104,109" fill="none" stroke="var(--chart-blue)" stroke-width="1.4"/>
        </svg>
        <div class="report-foot">Figures shown are sample values only</div>
      </article>

      <article class="report">
        <div class="report-head"><span>Agency loss report</span><span>Policy year review</span></div>
        <div class="report-title">Injury Analysis</div>
        <div role="img" aria-label="Illustration of a running figure with injury points" style="width:70px;height:66px;margin:4px auto 0;border-radius:50%;background:radial-gradient(circle,#cfe6f6,#eaf5fc)"></div>
        <svg width="110" height="40" viewBox="0 0 110 40" aria-hidden="true">
          <g fill="var(--chart-blue)">
            <rect x="20" y="18" width="8" height="14"/><rect x="38" y="10" width="8" height="22"/>
            <rect x="56" y="24" width="8" height="8"/><rect x="74" y="16" width="8" height="16"/>
          </g>
          <path d="M12 32H98" stroke="#ccc" stroke-width=".6"/>
        </svg>
        <div class="report-foot">Figures shown are sample values only</div>
      </article>

      <article class="report">
        <div class="report-head"><span>Agency loss report</span><span>Policy year review</span></div>
        <div class="report-title">Claims Analysis</div>
        <svg width="110" height="128" viewBox="0 0 110 128" aria-hidden="true">
          <g fill="none" stroke-width="7">
            <circle cx="42" cy="30" r="22" stroke="var(--chart-red)"/>
            <circle cx="42" cy="30" r="22" stroke="var(--chart-blue)" stroke-dasharray="40 99" stroke-dashoffset="-60"/>
            <circle cx="42" cy="30" r="22" stroke="var(--chart-green)" stroke-dasharray="22 99" stroke-dashoffset="-100"/>
            <circle cx="42" cy="30" r="22" stroke="var(--chart-yellow)" stroke-dasharray="8 130" stroke-dashoffset="-122"/>
            <circle cx="42" cy="88" r="22" stroke="var(--chart-red)"/>
            <circle cx="42" cy="88" r="22" stroke="var(--chart-blue)" stroke-dasharray="30 110" stroke-dashoffset="-40"/>
            <circle cx="42" cy="88" r="22" stroke="var(--chart-green)" stroke-dasharray="30 110" stroke-dashoffset="-70"/>
            <circle cx="42" cy="88" r="22" stroke="var(--chart-purple)" stroke-dasharray="10 130" stroke-dashoffset="-100"/>
            <circle cx="42" cy="88" r="22" stroke="var(--chart-yellow)" stroke-dasharray="10 130" stroke-dashoffset="-110"/>
          </g>
          <text x="42" y="32" font-size="5" text-anchor="middle" font-family="Jost, sans-serif">NATURE</text>
          <text x="42" y="90" font-size="5" text-anchor="middle" font-family="Jost, sans-serif">CAUSE</text>
          <g>
            <rect x="76" y="20" width="3" height="3" fill="var(--chart-red)"/><rect x="76" y="26" width="3" height="3" fill="var(--chart-blue)"/>
            <rect x="76" y="32" width="3" height="3" fill="var(--chart-green)"/><rect x="76" y="38" width="3" height="3" fill="var(--chart-yellow)"/>
            <rect x="76" y="78" width="3" height="3" fill="var(--chart-red)"/><rect x="76" y="84" width="3" height="3" fill="var(--chart-blue)"/>
            <rect x="76" y="90" width="3" height="3" fill="var(--chart-green)"/><rect x="76" y="96" width="3" height="3" fill="var(--chart-purple)"/>
          </g>
        </svg>
        <div class="report-foot">Figures shown are sample values only</div>
      </article>
    </div>
  </section>

  <div class="wall-monitor" aria-hidden="true"></div>

  <section class="counter">
    <div class="counter-top"></div>
    <div class="scene" role="img" aria-label="Concrete wall photo with a businesswoman casting a superhero shadow"></div>
    <div class="figure-area" role="img" aria-label="Businesswoman looking into the distance"></div>
    <span class="brand">trelvix</span>
  </section>

</body>
</html>
```